Business Card Design Project

We need a business card design for a company based in San Francisco called PlanGlide. PlanGlide makes customized academic planners for high schools and middle schools. Currently we sell directly to the schools who either re-sell or give the planners to their students. The planners are designed to help students stay organized and manage their time. The books are unique in that they are made individually for each school and include the school's events, student artwork and most importantly the daily class schedule in each week. This helps the student to understand what classes they have each day and what homework they need to do each night.

Currently the product is B:B; however, we are exploring ways in which to make this a B:C. Please review website at www.planglide.net

The final design should communicate time management and organization.

Card should be one-sided

Information for the business card should include

Dorothy Kellner Voss
Founder
dorothy@planglide.net
415-836-1752

Target Market(s)

High school and middle school administrators

Industry/Entity Type

School

Requirements
Must have
• One sided design
Nice to have
• I'm open to new interpretations of the logo as well as color usage. I'm also open to changing the font of the logo type.
Should not have
• Please use a san serif font.

```html
<!DOCTYPE html>
<html lang="en">
<head>
<meta charset="utf-8">
<title>PlanGlide Business Card</title>
<link rel="stylesheet" href="https://fonts.googleapis.com/css2?family=Fredoka:wght@600&family=Lato:wght@300;400&display=swap">
<style>
  :root {
    --page-bg: #e9e6e1;
    --card-teal: #1aa3b8;
    --card-teal-deep: #117f93;
    --card-teal-light: #2bbccd;
    --circle-tint: rgba(255, 255, 255, 0.07);
    --ink-white: #ffffff;
    --ink-dark: #0f4650;
    --dot-fill: #f2f5f7;
  }
  * { margin: 0; padding: 0; box-sizing: border-box; }
  html, body {
    width: 1200px;
    height: 1000px;
    overflow: hidden;
    background: var(--page-bg);
  }
  .canvas {
    position: relative;
    width: 1200px;
    height: 1000px;
  }
  .business-card {
    position: absolute;
    left: 100px;
    top: 215px;
    width: 1000px;
    height: 570px;
    overflow: hidden;
    border-radius: 6px;
    background: linear-gradient(135deg, var(--card-teal-deep) 0%, var(--card-teal) 45%, var(--card-teal-light) 75%, var(--card-teal) 100%);
    box-shadow: 0 18px 40px rgba(0, 0, 0, 0.18);
  }
  .backdrop-circle {
    position: absolute;
    left: 270px;
    top: 35px;
    width: 500px;
    height: 500px;
    border-radius: 50%;
    background: var(--circle-tint);
  }
  .brand-corner {
    position: absolute;
    left: 48px;
    top: 40px;
    color: var(--ink-dark);
  }
  .brand-name {
    font-family: "Lato", sans-serif;
    font-weight: 400;
    font-size: 30px;
    line-height: 1;
  }
  .brand-tagline {
    font-family: "Lato", sans-serif;
    font-weight: 300;
    font-size: 14px;
    margin-top: 4px;
    letter-spacing: 0.3px;
    color: var(--ink-white);
  }
  .brand-mark {
    position: absolute;
    left: 290px;
    top: 250px;
    display: flex;
    align-items: center;
    gap: 14px;
  }
  .mark-dot {
    width: 48px;
    height: 48px;
    border-radius: 50%;
    background: var(--dot-fill);
  }
  .mark-name {
    font-family: "Fredoka", sans-serif;
    font-weight: 600;
    font-size: 32px;
    line-height: 1;
    color: var(--ink-white);
  }
  .contact-block {
    position: absolute;
    left: 560px;
    top: 205px;
    color: var(--ink-white);
    font-family: "Fredoka", sans-serif;
    font-weight: 600;
    line-height: 1.3;
  }
  .person-name { font-size: 30px; }
  .person-role { font-size: 26px; padding-left: 90px; }
  .contact-email { font-size: 28px; margin-top: 14px; }
  .contact-phone { font-size: 28px; padding-left: 60px; }
</style>
</head>
<body>
  <main class="canvas">
    <section class="business-card">
      <div class="backdrop-circle"></div>

      <header class="brand-corner">
        <div class="brand-name">PlanGlide</div>
        <div class="brand-tagline">Customized Academic Planners</div>
      </header>

      <div class="brand-mark">
        <div class="mark-dot"></div>
        <div class="mark-name">PlanGlide</div>
      </div>

      <div class="contact-block">
        <div class="person-name">Dorothy Kellner Voss</div>
        <div class="person-role">Founder</div>
        <div class="contact-email">dorothy@planglide.net</div>
        <div class="contact-phone">415-836-1752</div>
      </div>
    </section>
  </main>
</body>
</html>
```